6" x 11" Print Mailer selling Fiber Internet Services

We need to design a 6" x 11" mailer offering Fiber Internet Services. People receiving this mailer are targeted specifically because fiber has been deployed in their neighborhoods and they can now sign up for fiber service to their door.

We want to lead with "Fiber is now at your door" to hammer home the fact that they can have fiber internet. The picture on the front should be a colorful set of fiber optic cables, the back side can be a happy family using a laptop or some device

We want to advertise two plans:

1) 250 Mbps for $34.95/mo
2) 1 Gbps for $46.95/mo

We need a small but obvious disclaimer that says "Plus $30 Meridane fees"

We want to offer a free month of service for signing up when they mention this mailer and to advertise our 24/7 Technical Support and No Long Term Commitments

We want our Logo (attached) phone number and website visible clearly on the front and back

555-304-2968
www.bravolink.co

Target Market(s)

Residential Households that have fiber internet services now available

Industry/Entity Type

Internet Service Provider

Font styles to use
Serif
Sans Serif
Other font styles liked:
• Futurona is the name of the font in our logo

Requirements
Must have
• Room for the NPMS to print the postage and address on the back. You can use this link for specific requirements from npms: https://about.npms-example.com/publications/pub600/pub600_006.htm
Nice to have
• Base the color scheme around our logo colors. This can be a vertical or horizontal (or vertical one side, horizontal on the other)
Should not have
• Do not replicate the mailer I have attached, we want something new - it is there for reference.

```html
<!DOCTYPE html>
<html lang="en">
<head>
<meta charset="utf-8">
<title>Bravolink Fiber Mailer</title>
<link rel="stylesheet" href="https://fonts.googleapis.com/css2?family=Roboto+Condensed:wght@400;700&family=Roboto:wght@400;500;700&family=Arimo:wght@400;700&display=swap">
<style>
  :root {
    --page-bg: #e6e8eb;
    --card-white: #ffffff;
    --brand-blue: #2a80cc;
    --band-blue: #2684cf;
    --navy: #1b1d3f;
    --teal: #2cb7a0;
    --sky: #8fc2e8;
    --pill: #d9e7f4;
    --ink: #222222;
    --ring: #9cc6e8;
  }
  * { margin: 0; padding: 0; box-sizing: border-box; }
  html, body { width: 1084px; height: 1200px; overflow: hidden; background: var(--page-bg); }
  body { position: relative; font-family: "Roboto", Arial, sans-serif; }

  .mailer {
    position: absolute; left: 42px; width: 1000px; height: 545px;
    background: linear-gradient(135deg, #f3f5f8 0%, #ffffff 45%, #f4f6f9 100%);
    overflow: hidden;
    box-shadow: 0 6px 16px rgba(0,0,0,0.22);
  }
  .mailer--front { top: 40px; }
  .mailer--back { top: 615px; background: linear-gradient(160deg, #ffffff 0%, #f6f7f9 60%, #eef1f4 100%); }

  .blue-band { position: absolute; left: 0; right: 0; top: 320px; bottom: 0; background: var(--band-blue); }

  .headline {
    position: absolute; left: 32px; top: 56px;
    font-family: "Roboto Condensed", "Arial Narrow", sans-serif; font-weight: 700;
    font-size: 57px; line-height: 69px; color: var(--brand-blue); letter-spacing: 0.5px;
  }

  .ring { position: absolute; border-radius: 50%; border: 1.5px solid var(--ring); }
  .photo {
    position: absolute; border-radius: 50%;
  }
  .photo--family {
    left: 461px; top: 33px; width: 464px; height: 464px;
    background: radial-gradient(circle at 55% 40%, #f1e2d2 0%, #d9c0a6 35%, #c8d6e4 70%, #e9eef3 100%);
  }
  .photo--laptop {
    left: -12px; top: -66px; width: 410px; height: 410px;
    background: radial-gradient(circle at 45% 45%, #dcdcdc 0%, #a9a9a9 45%, #6f6f6f 75%, #cfcfcf 100%);
  }

  .badge {
    position: absolute; border-radius: 50%;
    display: flex; flex-direction: column; align-items: center; justify-content: center;
    text-align: center; color: #fff;
  }
  .badge--offer { left: 371px; top: 188px; width: 236px; height: 236px; background: var(--navy); box-shadow: 0 0 0 4px rgba(255,255,255,0.35); }
  .offer-main { font-family: "Roboto", sans-serif; font-weight: 700; font-size: 40px; line-height: 38px; letter-spacing: 1px; }
  .offer-note { margin-top: 14px; font-weight: 500; font-size: 14px; line-height: 17px; letter-spacing: 1px; }

  .badge--plan-fast { left: 856px; top: 267px; width: 128px; height: 128px; background: var(--teal); }
  .badge--plan-gig { left: 758px; top: 342px; width: 160px; height: 160px; background: var(--sky); opacity: 0.95; }
  .plan-speed { font-size: 19px; font-weight: 500; }
  .plan-price { font-size: 16px; font-weight: 700; margin-top: 6px; }
  .plan-price sup { font-size: 9px; }
  .plan-fine { font-size: 7px; margin-top: 6px; }
  .badge--plan-gig .plan-speed { font-size: 22px; }
  .badge--plan-gig .plan-price { font-size: 18px; margin-top: 10px; }

  .badge--terms { left: 304px; top: 171px; width: 114px; height: 114px; background: var(--teal); font-family: "Roboto Condensed", sans-serif; font-weight: 700; font-size: 13px; line-height: 21px; }
  .badge--support { left: 214px; top: 238px; width: 130px; height: 130px; background: var(--sky); font-family: "Roboto Condensed", sans-serif; font-size: 16px; line-height: 22px; }
  .support-hours { font-size: 30px; line-height: 32px; }

  .brand {
    position: absolute; text-align: center; width: 360px;
  }
  .brand-name { display: flex; align-items: center; justify-content: center; gap: 10px; font-family: "Roboto", sans-serif; font-weight: 400; font-size: 52px; line-height: 56px; }
  .brand-dot { width: 20px; height: 20px; border-radius: 50%; }
  .brand-tagline { font-family: "Roboto", sans-serif; font-weight: 500; font-size: 24px; letter-spacing: 0.5px; margin-top: 2px; }
  .mailer--front .brand { left: 62px; top: 368px; color: #fff; }
  .mailer--front .brand-dot { background: #fff; }
  .mailer--back .brand { left: 100px; top: 375px; color: var(--brand-blue); }
  .mailer--back .brand-dot { background: var(--brand-blue); }

  .contact-pill {
    position: absolute; height: 32px; border-radius: 16px;
    display: flex; align-items: center; justify-content: center;
    font-family: "Roboto", sans-serif; font-weight: 500; font-size: 20px;
  }
  .mailer--front .contact-pill { left: 55px; top: 483px; width: 374px; background: var(--pill); color: var(--brand-blue); }
  .mailer--back .contact-pill { left: 91px; top: 477px; width: 375px; background: #5fa0dc; color: #fff; }

  .postage-indicia {
    position: absolute; left: 876px; top: 23px; width: 101px; height: 100px;
    border: 1px solid #444; font-family: "Arimo", Arial, sans-serif; font-size: 14px; line-height: 16.5px;
    color: var(--ink); text-align: center; padding-top: 10px;
  }
  .postage-indicia strong { font-weight: 700; }
  .address-block {
    position: absolute; left: 706px; top: 201px; width: 271px; height: 108px;
    border: 1px solid #444; font-family: "Arimo", Arial, sans-serif; color: var(--ink);
  }
  .address-route { position: absolute; right: 20px; top: 14px; font-size: 13px; }
  .address-name { position: absolute; left: 20px; top: 56px; font-size: 16px; line-height: 18px; }
</style>
</head>
<body>

<section class="mailer mailer--front" aria-label="Mailer front">
  <div class="blue-band"></div>
  <h1 class="headline">FIBER<br>IS NOW AT<br>YOUR DOOR</h1>
  <div class="ring" style="left:455px;top:27px;width:476px;height:476px;"></div>
  <div class="photo photo--family" role="img" aria-label="Photo of a happy family on a sofa sharing a tablet"></div>
  <div class="ring" style="left:363px;top:180px;width:252px;height:252px;border-color:rgba(255,255,255,0.6);"></div>
  <div class="badge badge--offer">
    <div class="offer-main">FIRST<br>MONTH<br>FREE</div>
    <div class="offer-note">WHEN MENTIONING<br>POSTCARD</div>
  </div>
  <div class="badge badge--plan-gig">
    <div class="plan-speed">1 Gbps</div>
    <div class="plan-price">for <sup>$</sup>46.95/mo</div>
  </div>
  <div class="badge badge--plan-fast">
    <div class="plan-speed">250 Mbps</div>
    <div class="plan-price">for <sup>$</sup>34.95/mo</div>
    <div class="plan-fine">Plus $30 Meridane fees</div>
  </div>
  <div class="brand">
    <div class="brand-name"><span class="brand-dot"></span>Bravolink</div>
    <div class="brand-tagline">Internet Services</div>
  </div>
  <div class="contact-pill">555-304-2968 | www.bravolink.co</div>
</section>

<section class="mailer mailer--back" aria-label="Mailer back">
  <div class="ring" style="left:-20px;top:-74px;width:426px;height:426px;"></div>
  <div class="photo photo--laptop" role="img" aria-label="Black and white photo of a father and son using a laptop"></div>
  <div class="badge badge--support">
    <div class="support-hours">24/7</div>
    <div>TECHNICAL<br>SUPPORT</div>
  </div>
  <div class="badge badge--terms">
    <div>NO LONG<br>TERM<br>COMMITMENTS</div>
  </div>
  <div class="brand">
    <div class="brand-name"><span class="brand-dot"></span>Bravolink</div>
    <div class="brand-tagline">Internet Services</div>
  </div>
  <div class="contact-pill">555-304-2968 | www.bravolink.co</div>

  <div class="postage-indicia">PRSRT STD<br>ECRWSS<br>U.S. Postage<br><strong>PAID</strong><br>EDDM RETAIL</div>
  <div class="address-block">
    <div class="address-route">****************ECRWSS****</div>
    <div class="address-name">Local<br>Postal Customer</div>
  </div>
</section>

</body>
</html>
```